Packaging design for Prenatal, Fish Oil, and Joint Pain product

We are looking for package design (label and outer box) for following products:
1) Merosa
- Product name: Merosa
- Benefit: Prenatal
- Feature DHA + Folic Acid
- What we need from you? We need box concept
- Box dimension 55mm Height x 145mm length x 100mm width
2) Omega 3 Alaskan Salmon
- Product name: Omega 3 Alaskan Salmon
- Benefit: Cognitive , cardiovascular Health, Joint Health, High cholesterol
- Feature: Alaskan Salmon
- What we need from you? We need label concept
- Label dimension: 60mm Height x 180mm Length
2) Ubrax
- Product name: Ubrax
- Benefit: Joint Health
- Feature: Glucosamin, Chondroitin, MSM
Designer can use generic text on other vitamin products for formula, usage instruction etc.
We have logo. The logo must be integrated in the packaging design. (please see attachment)

```html
<!DOCTYPE html>
<html lang="en">
<head>
<meta charset="utf-8">
<title>Merosa, Ubrax and Omega 3 packaging</title>
<link href="https://fonts.googleapis.com/css2?family=Montserrat:wght@300;400;500&family=Lora:ital,wght@1,600&family=Roboto:wght@400;700&family=Gelasio&display=swap" rel="stylesheet">
<style>
  :root {
    --ink: #4a3f40;
    --muted: #b9b9b9;
    --caption: #8a8a8a;
    --brand-red: #e0393f;
    --leaf-green: #7cc243;
    --box-pink: #e79aa2;
    --box-blue: #9ab5c9;
    --lavender: #e7deec;
    --magenta: #c23a8c;
    --soft-blue: #a8cfe0;
    --soft-pink: #e6a9c4;
    --joint-green: #8fdc45;
    --joint-green-text: #2ea82e;
    --heart-band: #6d85aa;
    --heart-blue: #2b5cf0;
    --heart-rule: #e2828a;
    --salmon-grey: #9db2c4;
  }
  * { box-sizing: border-box; margin: 0; padding: 0; }
  html, body { width: 1200px; height: 901px; overflow: hidden; background: #fff; }
  .sheet { position: relative; width: 1200px; height: 901px; font-family: "Montserrat", sans-serif; }
  .panel { position: absolute; background: #fff; overflow: hidden; }
  .panel--pink { border: 1px solid var(--box-pink); }
  .panel--blue { border: 1px solid var(--box-blue); }
  .abs { position: absolute; white-space: nowrap; }
  .mid { transform: translateX(-50%); text-align: center; }

  .brand { display: flex; align-items: center; gap: 3px; color: var(--brand-red);
           font-family: "Montserrat", sans-serif; font-weight: 500; line-height: 1; }
  .brand__dot { width: 9px; height: 9px; border-radius: 50%; background: var(--leaf-green); }

  .product-name { color: var(--ink); font-weight: 400; letter-spacing: 1px; line-height: 1; }
  .tagline { display: flex; align-items: center; gap: 6px; font-family: "Lora", serif;
             font-style: italic; font-weight: 600; color: var(--magenta); line-height: 1; }
  .tagline::before, .tagline::after { content: ""; flex: 1; height: 1px; background: currentColor; opacity: .6; }
  .feature { font-weight: 300; line-height: 1; }

  .fine { font-family: "Roboto", sans-serif; font-size: 8.5px; line-height: 12px; color: var(--muted); white-space: normal; }
  .fine b { color: #8a8a8a; font-weight: 700; }

  .caption { position: absolute; font-family: "Gelasio", serif; font-size: 15px; color: var(--caption); }

  .band { position: absolute; left: 0; right: 0; height: 8px; }
</style>
</head>
<body>
<main class="sheet">

  <!-- Box front -->
  <section class="panel panel--pink" style="left:27px;top:40px;width:455px;height:314px">
    <div role="img" aria-label="Soft lavender silhouette of a pregnant woman in profile" style="position:absolute;left:0;top:0;width:168px;height:100%;background:linear-gradient(90deg,var(--lavender),#efe8f2)"></div>
    <div class="abs brand" style="left:372px;top:45px;font-size:28px">nuvi<span class="brand__dot"></span></div>
    <div class="abs mid product-name" style="left:298px;top:133px;font-size:40px">MEROSA</div>
    <div class="abs mid tagline" style="left:298px;top:174px;width:172px;font-size:12px">Healthy pregnancy</div>
    <div class="abs mid feature" style="left:298px;top:196px;font-size:24px;color:var(--soft-blue)">DHA &amp; folic acid</div>
  </section>

  <!-- Box back -->
  <section class="panel panel--blue" style="left:504px;top:39px;width:455px;height:314px">
    <div class="abs brand" style="left:372px;top:45px;font-size:26px">nuvi<span class="brand__dot"></span></div>
    <div class="abs mid product-name" style="left:224px;top:52px;font-size:34px">MEROSA</div>
    <div class="abs mid tagline" style="left:224px;top:87px;width:144px;font-size:10px">Healthy pregnancy</div>
    <div class="abs feature" style="left:153px;top:107px;font-size:19px;color:var(--soft-pink)">DHA &amp; folic acid</div>
    <p class="abs fine" style="left:153px;top:145px;width:150px">DHA (docosahexaenoic acid) and Folic acid aids a healthy pregnancy as well as the mental and visual development of infants.</p>
    <p class="abs fine" style="left:153px;top:204px;width:140px"><b>Dose:</b> one capsule to be taken daily with a meal</p>
    <p class="abs fine" style="left:153px;top:240px;width:140px"><b>Ingredients:</b> docosahexaenoic acid and folic acid</p>
    <div class="abs feature" style="left:370px;top:273px;font-size:15px;color:#c9c9c9">100 mg</div>
  </section>

  <!-- Box side -->
  <section class="panel panel--pink" style="left:27px;top:374px;width:455px;height:173px">
    <div class="abs brand" style="left:378px;top:40px;font-size:26px">nuvi<span class="brand__dot"></span></div>
    <div class="abs mid product-name" style="left:227px;top:45px;font-size:38px">MEROSA</div>
    <div class="abs mid tagline" style="left:227px;top:89px;width:174px;font-size:12px">Healthy pregnancy</div>
    <div class="abs mid feature" style="left:227px;top:111px;font-size:23px;color:var(--soft-pink)">DHA &amp; folic acid</div>
  </section>

  <p class="caption" style="left:27px;top:557px">Front, back and side view of box</p>

  <!-- Bottle label: joints -->
  <section class="panel" style="left:27px;top:602px;width:565px;height:190px;border:1px solid #cfd9c4">
    <div class="band" style="top:0;background:var(--joint-green)"></div>
    <div class="band" style="bottom:0;background:var(--joint-green)"></div>
    <p class="abs fine" style="left:18px;top:72px;width:105px"><b>Dose:</b> one capsule to be taken daily with a meal</p>
    <p class="abs fine" style="left:18px;top:104px;width:105px"><b>Ingredients:</b> Glucosamin, Chondroitin</p>
    <div class="abs brand mid" style="left:285px;top:34px;font-size:24px">nuvi<span class="brand__dot"></span></div>
    <div class="abs mid product-name" style="left:282px;top:72px;font-size:46px">UBRAX</div>
    <div class="abs mid tagline" style="left:282px;top:122px;width:170px;font-size:12px;color:var(--joint-green-text)">Healthy joints</div>
    <div class="abs mid feature" style="left:282px;top:144px;font-size:12.5px;color:var(--salmon-grey)">Glucosamin, Chondroitin &amp; MSM</div>
  </section>

  <!-- Bottle label: heart -->
  <section class="panel" style="left:605px;top:602px;width:566px;height:190px;border:1px solid #c8d0dc">
    <div class="band" style="top:0;background:var(--heart-band)"></div>
    <div class="band" style="bottom:0;background:var(--heart-band)"></div>
    <p class="abs fine" style="left:18px;top:72px;width:105px"><b>Dose:</b> one capsule to be taken daily with a meal</p>
    <p class="abs fine" style="left:18px;top:104px;width:105px"><b>Ingredients:</b> Glucosamin, Chondroitin</p>
    <div class="abs brand mid" style="left:282px;top:34px;font-size:24px">nuvi<span class="brand__dot"></span></div>
    <div class="abs mid product-name" style="left:280px;top:72px;font-size:40px">OMEGA 3</div>
    <div class="abs mid tagline" style="left:280px;top:116px;width:176px;font-size:12px;color:var(--heart-blue)">Healthy heart</div>
    <div class="abs mid feature" style="left:282px;top:135px;font-size:24px;color:var(--salmon-grey)">Alaskan salmon</div>
  </section>

  <p class="caption" style="left:27px;top:799px">Bottle labels</p>

</main>
</body>
</html>
```